Letterhead Design for Law Firm

**Edit: I have added the photo of a bottom that I like.

------
We are looking for a re-design of our new letterhead. The letterhead is for a law firm and will be used for digital and traditionally printed correspondence.

Here are some suggestions:

- Please use colours are #8ec900 and simple black.
- Please do not use any type of "waves" at the bottom of the page. This is not in style at all.
- Please stay modern yet conservative.
- Please use font Segoe UI Light or similar if you can
- Avoid clipart or illustrations.
- Utilize ample white space in the layout so the design looks clean and information is easy to read at a glance. Don't overcrowd the letterhead.
- Make sure the letterhead design is consistent with our brand identity (see brambleford.ca)
-Please, no black headers or footers.

I am attaching my current letterhead and signature for your convenience.

Remember, the letterhead is an extension of our professional identity. We are a successful firm and trial lawyers who correspond with insurers, judges, lawyers, courts, clients, etc. Make it new, modern, attractive, yet powerful and conservative.

It needs to be easily printable. I would like the bleed removed in print so the black bar the bottom crosses the page (but the text is not near the edges)

Target Market(s)

Clients, Government Offices, Judiciary, Lawyers, Insurance Companies, Colleagues.

Industry/Entity Type

Law

Font styles to use
Other font styles liked:
• Segoe UI LIght, Calibri Light,

Colors
00AB8E
00BBA5
67D7C9
C6EFE9
E9F9F6

Requirements
Must have
• Everything that is on the letterhead now.
Nice to have
• Cutting Edge design, yet conservative.
Should not have
• law firm cliche design, images,

```html
<!DOCTYPE html>
<html lang="en">
<head>
<meta charset="utf-8">
<title>Ardent Personal Injury Lawyers – Letterhead</title>
<link href="https://fonts.googleapis.com/css2?family=Open+Sans:wght@400;700&display=swap" rel="stylesheet">
<style>
  :root {
    --brand-green: #8ec900;
    --ink: #111111;
    --paper: #ffffff;
    --wordmark: #ecebf0;
    --emblem: #e3f0c6;
    --signature-fill: #f1f1f1;
  }
  * { margin: 0; padding: 0; box-sizing: border-box; }
  html, body { width: 848px; height: 1200px; overflow: hidden; background: var(--paper); }
  body { font-family: "Open Sans", sans-serif; color: var(--ink); }
  .page { position: relative; width: 848px; height: 1200px; overflow: hidden; background: var(--paper); }

  .header-swoosh { position: absolute; left: 0; top: 0; width: 848px; height: 210px; }
  .wordmark {
    position: absolute; left: 72px; top: 34px;
    font-size: 60px; font-weight: 400; letter-spacing: 2px; color: var(--wordmark);
    line-height: 1; white-space: nowrap;
  }
  .emblem {
    position: absolute; left: 614px; top: 60px; width: 134px; height: 122px;
    border-radius: 50%; background: var(--emblem);
  }

  .field { position: absolute; left: 85px; width: 660px; font-size: 17px; line-height: 23.5px; }
  .label { position: absolute; left: 0; top: 0; font-weight: 700; white-space: nowrap; }
  .value { position: absolute; left: 101px; top: 0; white-space: nowrap; }
  .prejudice { top: 218px; font-weight: 700; white-space: nowrap; }
  .re-lines { font-weight: 700; }
  .rule { position: absolute; left: 85px; width: 648px; height: 1px; background: var(--ink); top: 598px; }

  .closing { position: absolute; left: 85px; top: 815px; font-size: 17px; line-height: 27px; white-space: nowrap; }
  .closing .firm { font-weight: 700; }
  .signature { position: absolute; left: 80px; top: 872px; width: 286px; height: 66px; background: var(--signature-fill); }
  .signatory { position: absolute; left: 85px; top: 942px; font-size: 17px; line-height: 21px; white-space: nowrap; }
  .signatory .corp { font-weight: 700; }

  .footer-rule { position: absolute; left: 85px; width: 648px; height: 1px; background: var(--brand-green); top: 1053px; }
  .footer-address { position: absolute; left: 85px; top: 1061px; font-size: 11px; white-space: nowrap; }
  .contact-row { position: absolute; left: 85px; top: 1085px; display: flex; font-size: 11.5px; align-items: center; white-space: nowrap; }
  .contact-item { display: flex; align-items: center; gap: 9px; }
  .contact-item svg { width: 16px; height: 14px; fill: var(--brand-green); }
  .contact-phone { width: 144px; }
  .contact-fax { width: 144px; }
  .contact-email { width: 188px; }
  .practice { position: absolute; left: 0; width: 876px; text-align: center; font-size: 11px; line-height: 15px; top: 1110px; }
  .bottom-band { position: absolute; left: 0; bottom: 0; width: 848px; height: 18px; background: var(--brand-green); }
</style>
</head>
<body>
<div class="page">
  <svg class="header-swoosh" viewBox="0 0 848 210" aria-hidden="true">
    <path fill="var(--brand-green)" d="M0,0 H848 V88 C760,52 660,40 585,48 C430,78 330,196 200,197 C110,198 40,150 0,108 Z"/>
    <path fill="#ffffff" d="M37,126 C100,170 160,182 220,179 C350,172 470,72 585,45 C480,66 380,150 230,172 C160,180 95,162 37,126 Z"/>
  </svg>
  <div class="wordmark">ARDENT</div>
  <div class="emblem" aria-hidden="true"></div>

  <div class="field prejudice">Without Prejudice</div>

  <div class="field" style="top:259px;">
    <span class="label">Date :</span>
    <span class="value" style="top:2px;">March 13th, 2024</span>
  </div>

  <div class="field" style="top:301px;">
    <span class="label">By Email :</span>
    <div class="value">Northvale Insurance Company<br>Claims Litigation Department<br>48 Alder Crescent North<br>P.O. Box 3100<br>Kitchener, ON&nbsp; N2K 5R7</div>
  </div>

  <div class="field" style="top:442px;">
    <span class="label">Attention :</span>
    <span class="value" style="left:103px;">Mr. Devon Hale</span>
  </div>

  <div class="field" style="top:481px;">
    <span class="value">Mr. Hale</span>
  </div>

  <div class="field re-lines" style="top:524px;">
    <span class="label" style="top:2px;">Re :</span>
    <div class="value" style="left:99px;">Marsh v. Corbett et al.<br><span style="margin-left:4px;">DOL:September 12, 2019</span><br><span style="margin-left:4px;">Pre-Mediation Settlement Proposal – March 13th, 2024</span></div>
  </div>

  <div class="rule"></div>

  <div class="closing">
    Yours very truly,<br>
    <span class="firm">ARDENT PERSONAL INJURY LAWYERS</span>
  </div>

  <div class="signature" role="img" aria-label="Handwritten signature of Colin J. Ardent"></div>

  <div class="signatory">
    Colin J. Ardent<br>
    <span class="corp">Ardent Law Professional Corporation</span><br>
    hh /<br>
    Encl.
  </div>

  <div class="footer-rule"></div>
  <div class="footer-address">27 Queen Street E., Suite 1210, Hamilton, ON L8N 2B6</div>

  <div class="contact-row">
    <div class="contact-item contact-phone">
      <svg viewBox="0 0 16 14"><path d="M1,4 C1,1 15,1 15,4 L15,6 L11,6 L11,4 L5,4 L5,6 L1,6 Z M3,7 H13 L14,13 H2 Z"/></svg>
      <span>905-555-0142</span>
    </div>
    <div class="contact-item contact-fax">
      <svg viewBox="0 0 16 14"><path d="M4,0 H12 V4 H15 V10 H12 V14 H4 V10 H1 V4 H4 Z M5,1 V4 H11 V1 Z M5,9 V13 H11 V9 Z"/></svg>
      <span>905-555-0187</span>
    </div>
    <div class="contact-item contact-email">
      <svg viewBox="0 0 16 14"><path d="M0,1 H16 V3 L8,8 L0,3 Z M0,4.5 L8,9.5 L16,4.5 V13 H0 Z"/></svg>
      <span style="margin-left:14px;">mira@brambleford.ca</span>
    </div>
    <div class="contact-item">
      <svg viewBox="0 0 16 16" style="height:14px;"><circle cx="8" cy="8" r="7" fill="none" stroke="var(--brand-green)" stroke-width="1.5"/><path d="M1,8 H15 M8,1 C4,5 4,11 8,15 M8,1 C12,5 12,11 8,15" fill="none" stroke="var(--brand-green)" stroke-width="1.2"/></svg>
      <span>www.BRAMBLEFORD.ca</span>
    </div>
  </div>

  <div class="practice">
    Practice Restricted - Serious Personal Injury - Wrongful Death Litigation<br>
    Long-Term Disability Litigation - Wrongful Dismissal Litigation -&nbsp; Employee Terminations
  </div>

  <div class="bottom-band"></div>
</div>
</body>
</html>
```